Martial Arts Website

Redevelopment of existing martial arts website.

The academy teaches traditional shaolin martial arts, including Shaolin Kung Fu, Wu Shu, Tai Chi, Qigong and Wing Chun and the site needs to reflect the traditional roots (eg, no tacky boxing imagery)

Existing website is www.copperheron.com.au to get a feel for the desired color scheme (black, green and red). The exact colors can be tweaked though. Please only reuse the logo and font (Karate) - there isnt anything else from the current design that needs to remain.

The current website includes links to a Clips channel that includes demonstrations of the training conducted to better guide the design.

The new website site map will be:
1. Home
2. Programs - summary page describing each form of training
a. Tiny Sparrows
b. Kids Kung Fu
c. Youth Kung Fu
d. Adults Kung Fu
e. Wing Chun
f. Tai Chi & Qigong
g. Weaponry Classes
h. 48 Paths of Mountain Endurance Program
i. Acrobatics and Wu Shu
j. Fitness Boxing
3. Timetable
4. Coaches - summary page describing all coaches
a. Sifu (Master)
b. Sihing Lars
c. Sihing Kit
d. Sihing Gordon
X. ... up to 10 or so coaches
5. Member Zone
6. Contact Us
Updates

Logo now attached to brief - sorry I only have it in PDF

Just to clarify, I am only expecting a PSD design - no HTML required

Project Deadline Extended
Reason: Thanks for the designs, we love a lot of them just require a little extra time to tweak the designs and establish the potential. Thanks for your understanding and efforts.

Target Market(s)

Parents, teenagers, young adults, adults, elderly

Industry/Entity Type

Training

Requirements
Must have
• Chinese kung fu dragon imagery throughout the background
Links to Social and Clips channel
Promo/icon in the header "Try 2 free classes now"
Home page should include an embedded Clips video

```html
<!DOCTYPE html>
<html lang="en">
<head>
<meta charset="utf-8">
<title>Copper Heron Martial Arts Academy</title>
<link href="https://fonts.googleapis.com/css2?family=Open+Sans:wght@400;600;700&family=Bangers&display=swap" rel="stylesheet">
<style>
:root{
  --bg:#141414;
  --bg-dark:#0b0b0b;
  --band:#1c1c1c;
  --green:#4fbf3a;
  --green-soft:#6dbb4e;
  --red:#d60d0d;
  --red-dark:#8a0000;
  --text:#e6e6e6;
  --muted:#9a9a9a;
  --link:#5fc24a;
}
*{margin:0;padding:0;box-sizing:border-box}
html,body{width:1200px;height:1103px;overflow:hidden}
body{background:radial-gradient(ellipse at 50% 40%,#262626 0%,var(--bg) 55%,#080808 100%);font-family:"Open Sans",sans-serif;color:var(--text);position:relative}
.site-title{position:absolute;top:10px;left:0;width:1200px;text-align:center;font-family:"Bangers",sans-serif;font-size:28px;letter-spacing:1px;color:var(--green)}
.nav-band{position:absolute;top:73px;left:0;width:1200px;height:50px;background:linear-gradient(#1e1e1e,#0e0e0e);border-top:1px solid #2a2a2a;border-bottom:1px solid #2a2a2a}
.nav{position:absolute;top:73px;left:0;width:1200px;height:50px;font-family:"Bangers",sans-serif;font-size:22px;color:var(--green);letter-spacing:1px}
.nav a{position:absolute;top:12px;text-decoration:none;color:inherit}
.nav a.active::after{content:"";position:absolute;left:-14px;right:-20px;top:35px;height:3px;background:var(--red)}
.nav .sep{position:absolute;top:14px;width:1px;height:24px;background:#333}
.emblem{position:absolute;left:533px;top:41px;width:128px;height:128px;border-radius:50%;background:#0a0a0a;border:5px solid var(--green);box-shadow:0 0 0 4px #000}
.hero{position:absolute;left:176px;top:123px;width:848px;height:295px}
.hero-photo{position:absolute;border-radius:4px}
.hero-tagline{position:absolute;left:165px;top:82px;font-weight:700;font-size:18.5px;line-height:25px;color:var(--green-soft)}
.dots{position:absolute;left:409px;top:280px;display:flex;gap:5px}
.dots span{width:10px;height:10px;border-radius:50%;background:#8fcf6c}
.dots span.on{background:#111}
.promo{position:absolute;left:176px;top:419px;width:848px;height:64px;border:1px solid #3a3a3a;background:linear-gradient(90deg,#2a2a2a,#111 25%,#111 75%,#2a2a2a)}
.promo-photo{position:absolute;top:0;height:62px}
.promo-title{position:absolute;left:138px;top:14px;font-weight:600;font-size:29px;color:#e0141a}
.promo-brand{position:absolute;left:514px;top:15px;font-family:"Bangers",sans-serif;font-size:12px;color:var(--green);letter-spacing:.5px}
.btn{display:inline-block;font-weight:700;font-size:11px;color:#fff;padding:3px 7px;border-radius:3px}
.btn-red{background:var(--red)}
.btn-green{background:#3a8a22}
.btn-dark{background:#111}
.promo .btn{position:absolute;left:514px;top:35px}
.card{position:absolute;top:504px;width:273px;height:289px;border-radius:3px;overflow:hidden}
.card h2{position:absolute;left:11px;top:6px;font-size:29px;font-weight:600;color:#fff}
.card p{position:absolute;left:11px;top:56px;width:256px;font-size:11.3px;line-height:17px;color:#f0f0f0}
.card .photo{position:absolute}
.card .btn{position:absolute}
.card-welcome{left:176px;background:radial-gradient(ellipse at 50% 80%,#ef2020,#b80000 70%,#900000)}
.card-why{left:464px;background:#060606}
.card-classes{left:751px;background:linear-gradient(#1a5a10,#3a5a12 50%,#6a5012)}
.card-classes ul{position:absolute;left:14px;top:50px;list-style:none;font-size:11.3px;line-height:20.6px}
.card-classes li::before{content:"";display:inline-block;width:4px;height:4px;border-radius:50%;background:#000;margin-right:8px;vertical-align:middle}
.lower{position:absolute;left:0;top:814px;width:1200px;height:240px;background:linear-gradient(90deg,transparent,rgba(10,10,10,.8) 15%,rgba(10,10,10,.8) 85%,transparent)}
.section-heading{position:absolute;top:827px;font-size:17.5px;font-weight:600;color:#fff;white-space:nowrap}
.video{position:absolute;left:186px;top:861px;width:246px;height:178px;background:#000}
.video-frame{position:absolute;left:0;top:0;width:246px;height:124px;background:linear-gradient(135deg,#3d6a3a,#7aa870 50%,#2c4a2a)}
.play{position:absolute;left:102px;top:48px;width:44px;height:30px;border-radius:6px;background:rgba(0,0,0,.8)}
.play::after{content:"";position:absolute;left:17px;top:8px;border-left:13px solid #fff;border-top:7px solid transparent;border-bottom:7px solid transparent}
.progress{position:absolute;left:0;top:142px;width:246px;height:4px;background:#c00}
.knob{position:absolute;left:3px;top:137px;width:13px;height:13px;border-radius:50%;background:#ddd}
.time{position:absolute;left:90px;top:158px;font-size:10px;color:#ddd}
.ctrl{position:absolute;left:22px;top:157px;border-left:11px solid #ccc;border-top:6px solid transparent;border-bottom:6px solid transparent}
.news{position:absolute;left:477px;width:262px;font-size:10.8px;line-height:16px;color:#ddd}
.news .date{float:left;background:var(--red);color:#fff;font-size:13px;padding:3px 8px;margin:2px 16px 4px 0;border-radius:2px}
.news a{color:var(--link);text-decoration:none}
.news-divider{position:absolute;left:477px;width:260px;height:1px;background:#2b2b2b}
.badge{position:absolute}
.side-tab{position:absolute;left:1144px;top:139px;width:56px;height:99px;background:#3a9a2a;border-radius:4px 0 0 4px}
.side-tab span{position:absolute;left:12px;width:38px;height:38px;border-radius:4px;background:#f2f2f2;font-size:10px;font-weight:700;color:#333;text-align:center;line-height:38px}
.footer{position:absolute;top:1076px;left:0;width:1200px;text-align:center;font-size:11px;color:var(--muted)}
.backdrop{position:absolute}
</style>
</head>
<body>
<div class="backdrop" role="img" aria-label="Faint Chinese dragon pattern in the background" style="left:0;top:160px;width:170px;height:320px;background:radial-gradient(ellipse,#222 0%,transparent 70%)"></div>
<div class="backdrop" role="img" aria-label="Martial artist throwing a punch at the right edge" style="left:1020px;top:800px;width:180px;height:303px;background:radial-gradient(ellipse at 80% 50%,#6a5040 0%,#2a2018 50%,transparent 80%)"></div>

<div class="site-title">Copper Heron Martial Arts Academy</div>

<div class="nav-band"></div>
<nav class="nav">
  <a style="left:178px">Home</a>
  <span class="sep" style="left:246px"></span>
  <a class="active" style="left:262px">Programs</a>
  <span class="sep" style="left:374px"></span>
  <a style="left:392px">Member Zone</a>
  <a style="left:675px">Coaches</a>
  <span class="sep" style="left:770px"></span>
  <a style="left:787px">Timetable</a>
  <span class="sep" style="left:897px"></span>
  <a style="left:914px">Contact Us</a>
</nav>

<section class="hero">
  <div class="hero-photo" role="img" aria-label="Children in white uniforms practising a flying kick and a throw" style="left:20px;top:10px;width:280px;height:285px;background:radial-gradient(ellipse at 40% 50%,#d8d8d8 0%,#6a6a6a 35%,transparent 70%)"></div>
  <div class="hero-photo" role="img" aria-label="Adult instructor in white uniform and black belt in a guarding stance" style="left:460px;top:0;width:388px;height:295px;background:radial-gradient(ellipse at 65% 55%,#e8e8e8 0%,#8a8a8a 35%,transparent 70%)"></div>
  <div class="hero-tagline">Practical, Responsible Instruction. Plus, we specialize in<br>perful character development skills in a positive env.</div>
  <div class="dots"><span></span><span></span><span class="on"></span><span></span></div>
</section>

<div class="emblem"></div>

<section class="promo">
  <div class="promo-photo" role="img" aria-label="Young student in training uniform" style="left:26px;width:100px;background:linear-gradient(90deg,#3a3a3a,#6a5a4a,#1a1a1a)"></div>
  <div class="promo-title">TRY 2 FREE CLASSES NOW</div>
  <div class="promo-brand">Copper Heron Martial Arts Academy</div>
  <span class="btn btn-red">TRY THE OPPORTUNITY NOW</span>
  <div class="promo-photo" role="img" aria-label="Instructor performing a high kick" style="left:740px;width:106px;background:linear-gradient(90deg,#1a1a1a,#5a5a5a,#2a2a2a)"></div>
</section>

<article class="card card-welcome">
  <h2>Welcome</h2>
  <p>Traditional Shaolin Kung Fu, Wing Chun Kung Fu, Tai Chi &amp; Qigong for all ages and physical capabilities. Qigong for all ages and physical capabilities.</p>
  <span class="btn btn-green" style="left:9px;top:150px">READ MORE</span>
  <div class="photo" role="img" aria-label="Two students practising a throw on the mat" style="left:80px;top:130px;width:190px;height:159px;background:radial-gradient(ellipse,#f2e8e8 0%,#d88080 45%,transparent 75%)"></div>
</article>
<article class="card card-why">
  <h2>Why Us</h2>
  <p>Traditional Shaolin Kung Fu, Wing Chun Kung Fu, Tai Chi &amp; Qigong for all ages and physical capabilities. Qigong for all ages and physical capabilities.</p>
  <span class="btn btn-red" style="left:13px;top:140px">READ MORE</span>
  <div class="photo" role="img" aria-label="Two practitioners in blue uniforms sparring" style="left:70px;top:120px;width:200px;height:169px;background:radial-gradient(ellipse,#3a5aa8 0%,#1a2a5a 45%,transparent 75%)"></div>
</article>
<article class="card card-classes">
  <h2>Classes</h2>
  <ul>
    <li>Tiny Sparrows - Ages 4 to 6</li>
    <li>Kids Kung Fu - Ages 6 to 11</li>
    <li>Youth Kung Fu - Ages 11 to 15</li>
    <li>Adults Kung Fu - Ages 15 &amp; over</li>
    <li>Wing Chun - Ages 13 &amp; over</li>
    <li>Tai Chi &amp; Qigong - All ages</li>
  </ul>
  <div class="photo" role="img" aria-label="Fighter in training gloves" style="left:140px;top:150px;width:133px;height:139px;background:radial-gradient(ellipse,#c09070 0%,#6a4a30 45%,transparent 75%)"></div>
  <span class="btn btn-dark" style="left:13px;top:194px">READ MORE</span>
</article>

<div class="lower"></div>
<h3 class="section-heading" style="left:187px">Latest Video</h3>
<h3 class="section-heading" style="left:478px">News &amp; Updates</h3>
<h3 class="section-heading" style="left:765px">Alliances &amp; Accreditation</h3>

<div class="video">
  <div class="video-frame" role="img" aria-label="Class training in a hall, video still"></div>
  <div class="play"></div>
  <div class="progress"></div>
  <div class="knob"></div>
  <div class="ctrl"></div>
  <div class="time">0:00</div>
</div>

<div class="news" style="top:859px"><span class="date">25.08.12</span>Traditional Shaolin Kung Fu, Wing Chun Kung Fu, Tai Chi &amp; Qigong for all ages and physical capabilities. Qigong for all ages and physical . <a>Read More</a></div>
<div class="news-divider" style="top:928px"></div>
<div class="news" style="top:934px"><span class="date">25.08.12</span>Traditional Shaolin Kung Fu, Wing Chun Kung Fu, Tai Chi &amp; Qigong for all ages and physical capabilities. <a>Read More</a></div>
<div class="news-divider" style="top:987px"></div>
<div class="news" style="top:999px"><span class="date">25.08.12</span>Traditional Shaolin Kung Fu, Wing Chun Kung Fu, Tai Chi &amp; Qigong for all ages and physical capabilities. <a>Read More</a></div>

<div class="badge" style="left:867px;top:862px;width:66px;height:76px;background:#8a8a8a"></div>
<div class="badge" style="left:765px;top:953px;width:75px;height:50px;background:#f2f2f2"></div>
<div class="badge" style="left:868px;top:946px;width:66px;height:66px;border-radius:50%;background:#d8b040;border:4px solid #222"></div>
<div class="badge" style="left:961px;top:950px;width:62px;height:49px;background:#e8e8ee"></div>

<div class="side-tab">
  <span style="top:9px">Social</span>
  <span style="top:54px">Clips</span>
</div>

<div class="footer">Copyright © 2012 - Copper Heron Martial Arts Pty Ltd. North Ridgeton NSW 2799</div>
</body>
</html>
```